Church Bulletin Ad (see attached sample)

Create a New Church Bulletin Ad. I have attached some samples of what we would like to have in the ad. (1) Marrowfield Realty Quist Logo (2) Headshot (3) Lorna Tavish & Greta Tavish, Real Estate Team (4) Phone number (5) Email address (6) St Agathe Parishioners for over 40 Years. We would like for the ad to be clean and modern. NO OTHER IMAGES besides headshots and Marrowfield Realty Quist Logo.

Target Market(s)

Church community

Industry/Entity Type

Real Estate

Font styles to use
Sans Serif
Other font styles liked:
• Modern Font

Colors
0054AA
0677BA
7BADD7
CADEEF
E8F1F8

Requirements
Must have
• Marrowfield Realty Quist Logo; Headshot; Ad size is 4.5"x1.62"

```html
<!DOCTYPE html>
<html lang="en">
<head>
<meta charset="utf-8">
<title>Tavish Real Estate Team – Bulletin Ad</title>
<link rel="stylesheet" href="https://fonts.googleapis.com/css2?family=Oswald:wght@700&family=Tinos:wght@400;700&family=Open+Sans:wght@600;700&display=swap">
<style>
  :root {
    --page-grey: #d4d4d4;
    --navy: #0b2248;
    --navy-deep: #081a3a;
    --navy-soft: #1a3a68;
    --sky: #3bb8ec;
    --swoosh-dark: #0677ba;
    --swoosh-light: #1d9fdc;
    --white: #ffffff;
    --placeholder: #3e5a82;
    --placeholder-edge: #4d6a93;
  }
  * { margin: 0; padding: 0; box-sizing: border-box; }
  html, body {
    width: 1200px; height: 516px; overflow: hidden;
    background: var(--page-grey);
  }
  .ad {
    position: absolute; left: 71px; top: 71px;
    width: 1057px; height: 380px; overflow: hidden;
    background: var(--navy);
    font-family: "Open Sans", sans-serif; color: var(--white);
  }
  .backdrop-glow {
    position: absolute; left: 0; top: 0; width: 680px; height: 380px;
    background: linear-gradient(90deg, var(--navy-soft) 0%, var(--navy-soft) 55%, var(--navy) 100%);
  }
  .headshot {
    position: absolute; bottom: 0;
    border-radius: 46% 46% 0 0 / 30% 30% 0 0;
    background: linear-gradient(180deg, var(--placeholder-edge) 0%, var(--placeholder) 100%);
  }
  .headshot--lorna { left: 0; width: 258px; height: 293px; }
  .headshot--greta { left: 258px; width: 262px; height: 302px; }
  .swoosh { position: absolute; left: 0; top: 0; }
  .headline {
    position: absolute; left: 503px; top: 40px; width: 504px;
    font-family: "Oswald", sans-serif; font-weight: 700;
    font-size: 38px; line-height: 1; letter-spacing: -0.2px;
    color: var(--sky); text-align: center; white-space: nowrap;
  }
  .team-name {
    position: absolute; left: 540px; top: 93px; width: 436px;
    font-family: "Tinos", serif; font-size: 29px; line-height: 36px;
    text-align: center; letter-spacing: 0.6px;
  }
  .brand-mark {
    position: absolute; left: 564px; top: 190px; width: 84px; height: 80px;
    border: 3px solid var(--white); background: var(--navy-deep);
    display: flex; align-items: center; justify-content: center; text-align: center;
    font-size: 11px; font-weight: 700; line-height: 14px; padding: 4px;
  }
  .contact { position: absolute; left: 660px; }
  .contact--phone { top: 202px; display: flex; align-items: center; gap: 10px; }
  .contact--email { top: 238px; display: flex; align-items: center; gap: 12px; }
  .phone-number { font-size: 35px; font-weight: 700; line-height: 1; letter-spacing: 0.3px; }
  .email-address { font-size: 17px; font-weight: 700; line-height: 1; }
  .parish-line {
    position: absolute; left: 565px; top: 284px;
    display: flex; align-items: baseline; gap: 9px; white-space: nowrap;
  }
  .parish-line__lead { font-size: 15.3px; font-weight: 700; }
  .parish-line__years { font-size: 26.5px; font-weight: 700; color: var(--sky); }
</style>
</head>
<body>
  <div class="ad">
    <div class="backdrop-glow" aria-hidden="true"></div>

    <svg class="swoosh" width="1057" height="380" viewBox="0 0 1057 380" aria-hidden="true">
      <path d="M1057 116 C1030 200 1000 300 955 380 L1057 380 Z" fill="var(--swoosh-light)"/>
      <path d="M518 380 C700 360 900 340 1057 296 L1057 380 Z" fill="var(--swoosh-dark)"/>
      <path d="M955 380 C1000 330 1030 310 1057 296 L1057 380 Z" fill="var(--swoosh-light)"/>
    </svg>

    <div class="headshot headshot--lorna" role="img" aria-label="Headshot of Lorna Tavish"></div>
    <div class="headshot headshot--greta" role="img" aria-label="Headshot of Greta Tavish"></div>

    <h1 class="headline">ENERGY EXCELLENCE EXPERIENCE</h1>
    <p class="team-name">Lorna Tavish &amp; Greta Tavish,<br>Real Estate Team</p>

    <div class="brand-mark">Marrowfield Realty Quist</div>

    <div class="contact contact--phone">
      <svg width="24" height="24" viewBox="0 0 24 24" aria-hidden="true">
        <path d="M6.6 3.5l2.6 3.8-1.8 2a11 11 0 0 0 7.3 7.3l2-1.8 3.8 2.6-1.2 3.2C11.5 20.8 3.2 12.5 3.4 4.7z" fill="var(--white)"/>
        <path d="M14 3.5a6.5 6.5 0 0 1 6.5 6.5M14 7a3 3 0 0 1 3 3" stroke="var(--white)" stroke-width="1.8" fill="none" stroke-linecap="round"/>
      </svg>
      <span class="phone-number">(555) 014-2387</span>
    </div>

    <div class="contact contact--email">
      <svg width="17" height="13" viewBox="0 0 17 13" aria-hidden="true">
        <rect x="0" y="0" width="17" height="13" fill="var(--white)"/>
        <path d="M0.8 0.8l7.7 6.3 7.7-6.3M0.8 12.2l5.6-5.3M16.2 12.2l-5.6-5.3" stroke="var(--navy)" stroke-width="1.3" fill="none"/>
      </svg>
      <span class="email-address">TavishTeam@MQRealty.com</span>
    </div>

    <p class="parish-line">
      <span class="parish-line__lead">St Agathe Parishioners for</span>
      <span class="parish-line__years">over 40 Years</span>
    </p>
  </div>
</body>
</html>
```